Internet Of Things brochure

Need to create a brochure with a common theme to our website and the last 2 pages of the attached file. All the contect is in the file that I have attached.
website www.norvalenetworks.com.au

Industry/Entity Type

Internet

```html
<!DOCTYPE html>
<html lang="en">
<head>
<meta charset="UTF-8">
<title>Norvale Networks – Smart Cities Initiative Brochure</title>
<link href="https://fonts.googleapis.com/css2?family=Exo+2:wght@400;500;600&display=swap" rel="stylesheet">
<style>
  :root {
    --backdrop: #ffffff;
    --cover-grey-top: #c9cad8;
    --cover-grey-bottom: #d8d9e4;
    --ink-black: #050506;
    --brand-blue: #1d3f78;
    --brand-blue-light: #3c6aa6;
    --band-blue-dark: #173f73;
    --band-blue-light: #3a689e;
    --photo-light: #d9dee6;
    --photo-mid: #8f9bb0;
    --photo-dark: #2c3347;
    --white: #ffffff;
    --badge-grey: #bfc3cc;
  }

  * { box-sizing: border-box; margin: 0; padding: 0; }

  html, body {
    width: 1200px;
    height: 1000px;
    overflow: hidden;
    background: var(--backdrop);
    font-family: "Exo 2", sans-serif;
  }

  .spread {
    position: absolute;
    left: 100px;
    top: 146px;
    width: 1000px;
    height: 707px;
    display: flex;
    box-shadow: 0 18px 40px rgba(0,0,0,0.18);
  }

  .page {
    position: relative;
    width: 500px;
    height: 707px;
    overflow: hidden;
  }

  /* Back cover */
  .back-cover {
    background: linear-gradient(180deg, var(--cover-grey-top), var(--cover-grey-bottom));
  }

  .back-cover .invite {
    position: absolute;
    top: 250px;
    left: 0;
    width: 100%;
    text-align: center;
    color: var(--brand-blue);
  }

  .invite-question {
    font-size: 19px;
    font-weight: 500;
    letter-spacing: 0.2px;
  }

  .invite-call {
    margin-top: 10px;
    font-size: 24px;
    font-weight: 600;
  }

  .back-footer {
    position: absolute;
    left: 0;
    bottom: 0;
    width: 100%;
    height: 250px;
    background: var(--ink-black);
    display: flex;
    flex-direction: column;
    align-items: center;
    justify-content: center;
    gap: 14px;
  }

  .brand-mark {
    display: flex;
    align-items: center;
    gap: 10px;
    color: var(--brand-blue-light);
    font-size: 24px;
    font-weight: 600;
  }

  .brand-square {
    width: 22px;
    height: 22px;
    background: var(--brand-blue-light);
  }

  .back-contact {
    text-align: center;
    color: var(--white);
    font-size: 14px;
    line-height: 1.4;
  }

  /* Front cover */
  .front-cover {
    background: var(--ink-black);
  }

  .title-band {
    height: 112px;
    background: linear-gradient(90deg, var(--band-blue-light), var(--band-blue-dark) 70%);
    display: flex;
    align-items: flex-end;
    padding: 0 0 10px 28px;
  }

  .cover-title {
    color: var(--white);
    font-size: 15px;
    font-weight: 500;
  }

  .cover-photo {
    height: 318px;
    background: linear-gradient(120deg, var(--photo-light) 0%, var(--photo-mid) 50%, var(--photo-dark) 100%);
  }

  .front-footer {
    position: relative;
    height: 277px;
    padding: 14px 20px 0 28px;
  }

  .front-contact {
    text-align: right;
    color: var(--white);
    font-size: 11px;
    line-height: 1.35;
  }

  .front-contact .web { margin-top: 10px; }

  .partner-row {
    position: absolute;
    left: 28px;
    top: 82px;
    display: flex;
    align-items: center;
    gap: 16px;
  }

  .partner-row .brand-mark {
    color: var(--white);
    font-size: 13px;
    gap: 6px;
  }

  .partner-row .brand-square {
    width: 12px;
    height: 12px;
    background: var(--white);
  }
</style>
</head>
<body>
  <main class="spread">
    <section class="page back-cover">
      <div class="invite">
        <p class="invite-question">Interested in discovering your digital opportunities?</p>
        <p class="invite-call">Let’s talk - 1300 555 019</p>
      </div>
      <footer class="back-footer">
        <div class="brand-mark"><span class="brand-square"></span>Norvale Networks</div>
        <div class="back-contact">
          <p>info@norvalenetworks.com.au</p>
          <p>www.norvalenetworks.com.au</p>
        </div>
      </footer>
    </section>

    <section class="page front-cover">
      <header class="title-band">
        <h1 class="cover-title">Smart Cities Initiative</h1>
      </header>
      <div class="cover-photo" role="img" aria-label="Photograph of two business colleagues reviewing a tablet at a bright office desk"></div>
      <footer class="front-footer">
        <div class="front-contact">
          <p>P: 1300 555 019</p>
          <p>A: 48 - 52 Carrow Road</p>
          <p>Kelsford, NSW, 2190</p>
          <p class="web">W: norvalenetworks.au</p>
        </div>
        <div class="partner-row">
          <div class="brand-mark"><span class="brand-square"></span>Norvale</div>
          <svg width="60" height="26" aria-label="Partner badge" role="img"><rect x="0" y="3" width="60" height="20" rx="3" fill="var(--badge-grey)"/></svg>
          <svg width="76" height="26" aria-label="Cloud partner badge" role="img"><rect x="0" y="3" width="76" height="20" rx="3" fill="var(--badge-grey)"/></svg>
        </div>
      </footer>
    </section>
  </main>
</body>
</html>
```